Copperleaf Vantage Training PowerPoint Template

I want to PowerPoint template theme using my attached logo. My colors are black and orange. My website is CopperleafVantage.com. I am a handgun training company.

Font:

- Serpentine-Bold-Bold for "IRON BRAE"

- BrowalliaUPC for "SHOOTING SPORTS"

Colors (CMYK code):

- BLACK ....... 0; 0; 0; 100;
- ORANGE ... gradient from 0; 65; 97.5; 0 to 0; 39; 97.5; 0

```html
<!DOCTYPE html>
<html lang="en">
<head>
<meta charset="UTF-8">
<title>Copperleaf Vantage Training – Closing Slide</title>
<link href="https://fonts.googleapis.com/css2?family=Carlito:wght@400;700&display=swap" rel="stylesheet">
<style>
  :root {
    --slide-bg: #262626;
    --footer-black: #000000;
    --orange: #f28c00;
    --orange-deep: #e06f00;
    --orange-bright: #ffb400;
    --silver: #b5b5b5;
    --placeholder-grey: #8c8c8c;
    --frame-line: #d9d9d9;
    --text-white: #ffffff;
  }
  * { margin: 0; padding: 0; box-sizing: border-box; }
  html, body {
    width: 1200px; height: 676px; overflow: hidden;
    background: var(--slide-bg);
  }
  .slide {
    position: relative; width: 1200px; height: 676px;
    background: var(--slide-bg);
    font-family: "Carlito", "Calibri", sans-serif;
    overflow: hidden;
  }
  .frame {
    position: absolute;
    border: 1px dashed var(--frame-line);
  }
  .photo-slot {
    left: 67px; top: 66px; width: 296px; height: 356px;
  }
  .photo-slot__prompt {
    position: absolute; left: 9px; top: 4px; right: 8px;
    font-size: 35px; line-height: 44px;
    color: var(--placeholder-grey);
    text-shadow: 2px 2px 3px rgba(0,0,0,0.55);
  }
  .photo-slot__icon {
    position: absolute; left: 130px; top: 161px;
  }
  .title-frame {
    left: 427px; top: 66px; width: 409px; height: 99px;
  }
  .title {
    position: absolute; left: 10px; top: 14px;
    font-size: 61px; line-height: 66px; font-weight: 400;
    color: var(--orange);
  }
  .name-frame {
    left: 424px; top: 239px; width: 359px; height: 36px;
  }
  .presenter-name {
    position: absolute; left: 8px; top: 4px;
    font-size: 22px; line-height: 26px; font-weight: 700;
    color: var(--orange);
  }
  .credentials {
    position: absolute; left: 433px; top: 280px;
    list-style: none;
    color: var(--text-white);
    font-size: 16.5px; line-height: 30px;
  }
  .accent-band {
    position: absolute; left: 0; top: 599px; width: 1200px; height: 17px;
  }
  .accent-band__silver {
    height: 5px;
    background: linear-gradient(90deg, #8a8a8a 0%, var(--silver) 50%, #8a8a8a 100%);
  }
  .accent-band__orange {
    height: 12px;
    background: linear-gradient(90deg, var(--orange-deep) 0%, var(--orange-bright) 50%, var(--orange-deep) 100%);
  }
  .footer {
    position: absolute; left: 0; top: 616px; width: 1200px; height: 60px;
    background: var(--footer-black);
  }
  .page-number {
    position: absolute; left: 1134px; top: 10px;
    font-size: 12px; font-weight: 700; color: var(--text-white);
  }
</style>
</head>
<body>
  <main class="slide">
    <div class="frame photo-slot">
      <p class="photo-slot__prompt">Click icon to add picture</p>
      <svg class="photo-slot__icon" width="36" height="34" viewBox="0 0 36 34" aria-hidden="true">
        <rect x="1" y="1" width="27" height="25" fill="#7d7d7d" stroke="#a8a8a8"/>
        <circle cx="21" cy="8" r="3" fill="#c8a060"/>
        <polygon points="2,25 11,14 18,21 22,17 27,25" fill="#5e5e5e"/>
        <rect x="15" y="14" width="20" height="15" fill="#4a5a6e" stroke="#cfd6df"/>
        <rect x="17" y="16" width="16" height="10" fill="#7c93ad"/>
        <rect x="21" y="29" width="8" height="3" fill="#cfd6df"/>
      </svg>
    </div>

    <div class="frame title-frame">
      <h1 class="title">Thank You!</h1>
    </div>

    <div class="frame name-frame">
      <h2 class="presenter-name">Dale Hollis</h2>
    </div>

    <ul class="credentials">
      <li>NMG Certified Instructor</li>
      <li>State of Tennessee Certified Handgun Instructor</li>
      <li>555-014-2273</li>
      <li>r.dale.hollis@fastpost.com</li>
      <li>www.CopperleafVantage.com</li>
    </ul>

    <div class="accent-band">
      <div class="accent-band__silver"></div>
      <div class="accent-band__orange"></div>
    </div>
    <footer class="footer">
      <span class="page-number">5</span>
    </footer>
  </main>
</body>
</html>
```